Website for Ledger Halcyon a cyrpto Mining company that sells crypto mining rigs

β€œIn the age of de-centralised financial services, individuals with a relatively small investment can use their own hardware to process crypto transactions and earn a substantial second income.”

Ledger Halcyon provide a personal home and hosted mining solutions to enable individuals to earn monthly crypto currencies of today and the future.”
Home/Products/About
Images – I had assumed this was part of the Design? For the home page I have a 10 second video of blockchain. I can only find on Pixelbarrow For any text or sections please refer to our old website www.thirdheron.ae
https://www.pixelbarrow.com/video/clip-4729301856-block-chain-concept---consists-network-connections I can buy and send?
On each page I will have a video similar, can you just put placeholder images and videos. I can replace. I am pretty good with Wordpress.
Updates

Please use text from my old website www.thirdheronmining.com

Target Market(s)

High Net wealth interested in Crypto

Industry/Entity Type

Crypto Mining

Coding

Coded - Design and coding required

Number of Pages Required

5+ page

Font styles to use
Other font styles liked:
• Sansation

Colors
0054AA
0677BA
7BADD7
CADEEF
E8F1F8

Requirements
Must have
• Video as banner (Will supply Video), Wordpress
Nice to have
• Will need Member login and Shop in future, please ensure this will be possible. (But not part of this project)

```html
<!DOCTYPE html>
<html lang="en">
<head>
<meta charset="utf-8">
<title>Ledger Halcyon – Crypto Mining</title>
<link href="https://fonts.googleapis.com/css2?family=Lato:wght@300;400;700;900&display=swap" rel="stylesheet">
<style>
:root{
  --blue-deep:#0054AA;
  --blue:#0677BA;
  --blue-band:#0b60b0;
  --blue-testi:#1464bd;
  --blue-soft:#6a9fd5;
  --blue-pale:#CADEEF;
  --blue-mist:#E8F1F8;
  --grey-bg:#f4f2f3;
  --ink:#1d1d1f;
  --text:#444;
  --night:#0b0d2e;
  --footer:#1c1c20;
  --accent:#f2a21b;
}
*{margin:0;padding:0;box-sizing:border-box}
html,body{width:1200px;height:4619px;overflow:hidden}
body{font-family:'Lato',sans-serif;color:var(--text);background:#fff;position:relative}
section,header,footer{position:absolute;left:0;width:1200px}
.abs{position:absolute}
.logo{display:flex;align-items:center;gap:14px;color:#1f7de0;font-weight:900;letter-spacing:2px}
.logo-mark{width:38px;height:38px;background:#1f7de0;border-radius:4px}
.nav{display:flex;gap:0;font-size:15px;letter-spacing:.5px;color:#fff}
.nav a{color:inherit;text-decoration:none;position:absolute;white-space:nowrap}
.section-title{position:absolute;left:0;width:1200px;text-align:center;font-weight:700;font-size:25px;color:var(--ink);letter-spacing:.3px}
.rule{position:absolute;width:58px;height:10px}
.rule::before{content:"";position:absolute;left:0;top:4px;width:54px;height:2px;background:var(--blue)}
.rule::after{content:"";position:absolute;right:0;top:1px;width:9px;height:9px;border-radius:50%;background:var(--blue)}
.rule.light::before,.rule.light::after{background:#fff}

/* hero */
.hero{top:0;height:700px;background:linear-gradient(180deg,#070a24 0%,#0d1343 55%,#0a0f33 100%)}
.hero-media{position:absolute;left:0;top:140px;width:1200px;height:500px;background:radial-gradient(ellipse 360px 220px at 605px 250px,#1aa2ff 0%,#0d64d6 40%,rgba(13,40,120,.35) 75%,transparent 100%),linear-gradient(90deg,rgba(30,140,255,.35),rgba(30,120,255,.05) 40%,rgba(30,120,255,.05) 70%,rgba(30,140,255,.25))}
.play{position:absolute;left:571px;top:347px}

/* services */
.services{top:700px;height:753px;background:var(--grey-bg)}
.tile{position:absolute;top:161px;width:144px;height:158px;background:#fff;text-align:center;font-size:13px;line-height:17px;color:#333}
.tile svg{display:block;margin:26px auto 18px}
.tile.active{background:var(--blue-deep);color:#fff}
.service-art{position:absolute;left:135px;top:376px;width:493px;height:305px;background:radial-gradient(ellipse at 50% 55%,#3d5bff 0%,#8fa2ff 35%,#e6e8fb 70%,transparent 100%)}
.service-copy{position:absolute;left:716px;top:413px;width:345px}
.service-copy h3{font-size:24px;font-weight:700;color:var(--ink);margin-bottom:22px}
.service-copy p{font-size:15px;line-height:26px;color:#444}

/* welcome */
.welcome{top:1453px;height:526px;background:var(--blue-band);overflow:hidden}
.welcome-art{position:absolute;left:592px;top:0;width:608px;height:526px;background:linear-gradient(90deg,var(--blue-band) 0%,rgba(11,96,176,.3) 25%,#0e1a30 55%,#231116 100%)}
.welcome .kicker{position:absolute;left:126px;top:59px;color:#fff;font-size:18px;font-weight:700}
.welcome h2{position:absolute;left:126px;top:87px;color:#fff;font-size:38px;font-weight:700;letter-spacing:.5px}
.welcome p{position:absolute;left:129px;top:203px;width:462px;color:#fff;font-size:15.5px;line-height:26px}
.btn{position:absolute;display:flex;align-items:center;justify-content:center;font-size:13px;font-weight:700;letter-spacing:.3px}
.btn-white{background:#fff;color:var(--blue-deep)}
.btn-blue{background:var(--blue-deep);color:#fff}

/* team */
.team{top:1979px;height:734px;background:#fff}
.member{position:absolute;top:158px;width:298px;height:490px;border:1px solid #7fb0e0;text-align:center}
.member .photo{height:308px;background:linear-gradient(160deg,#d8d4cf,#8a8580 60%,#3e3c3b)}
.member h4{margin-top:36px;font-size:16px;font-weight:700;color:var(--ink)}
.member p{margin:17px auto 0;width:250px;font-size:13px;line-height:19px;color:#555}
.member .btn{left:90px;top:468px;width:118px;height:38px}

/* sells */
.sells{top:2713px;height:464px;background:var(--grey-bg)}
.gpu-art{position:absolute;left:144px;top:50px;width:394px;height:386px;background:radial-gradient(ellipse at 55% 45%,#3b3b3e 0%,#1e1e20 45%,#b8b6b6 75%,transparent 90%)}
.sells h3{position:absolute;left:619px;top:58px;font-size:25px;font-weight:700;color:var(--ink)}
.sells p{position:absolute;left:619px;top:158px;width:415px;font-size:15px;line-height:26px;color:#444}

/* testimonials */
.testimonials{top:3177px;height:583px;background:linear-gradient(180deg,#1769c4,#0f5bb2)}
.testimonials .section-title{color:#fff}
.quote{position:absolute;top:153px;width:298px;height:375px;border:1px solid rgba(255,255,255,.7);color:#fff;padding:18px 32px 0}
.quote .mark{font-size:34px;font-weight:900;line-height:28px;height:22px}
.quote p{font-size:13.4px;line-height:19.7px}
.quote cite{position:absolute;left:32px;bottom:32px;font-style:normal;font-size:11px;font-weight:700;letter-spacing:.2px}
.arrow{position:absolute;top:3503px}

/* faq */
.faq{top:3760px;height:415px;background:#fff}
.q{position:absolute;width:464px;border:1px solid #c6c6c6;display:flex;align-items:center;justify-content:space-between;padding:0 16px 0 20px;font-size:12.5px;color:#333}
.q svg{flex:none}

/* cta */
.cta{top:4175px;height:188px;background:var(--blue-soft)}
.cta p{position:absolute;left:131px;top:50px;width:470px;color:#fff;font-size:27px;font-weight:300;line-height:36px}
.cta .btn{left:858px;top:54px;width:211px;height:73px;font-size:20px;font-weight:900}

/* footer */
.site-footer{top:4363px;height:256px;background:var(--footer)}
.site-footer .follow{position:absolute;left:830px;top:62px;color:#fff;font-size:13px}
.social{position:absolute;top:53px;width:32px;height:32px;border-radius:50%;background:var(--blue-deep)}
.site-footer .line{position:absolute;left:131px;top:170px;width:940px;height:1px;background:#444}
.site-footer .copy{position:absolute;left:0;top:210px;width:1200px;text-align:center;color:#ccc;font-size:13px}
</style>
</head>
<body>

<header class="hero">
  <div class="hero-media" role="img" aria-label="Banner video placeholder: glowing blue blockchain cube linked by chains"></div>
  <div class="logo abs" style="left:129px;top:52px;font-size:30px"><span class="logo-mark"></span>LEDGER HALCYON</div>
  <nav class="nav">
    <a style="left:676px;top:59px">HOME</a>
    <a style="left:775px;top:59px">SERVICES</a>
    <a style="left:908px;top:59px">FAQ</a>
    <a style="left:987px;top:59px">CONTACT</a>
  </nav>
  <svg class="play" width="64" height="64" viewBox="0 0 64 64" aria-label="Play video"><circle cx="32" cy="32" r="32" fill="var(--accent)"/><path d="M25 19 L46 32 L25 45 Z" fill="#fff"/></svg>
</header>

<section class="services">
  <h2 class="section-title" style="top:48px">OUR SERVICES</h2>
  <span class="rule" style="left:570px;top:97px"></span>

  <div class="tile active" style="left:129px">
    <svg width="44" height="44" viewBox="0 0 44 44" fill="none" stroke="#fff" stroke-width="2"><rect x="3" y="3" width="38" height="38" rx="3"/><circle cx="22" cy="22" r="13"/><circle cx="22" cy="22" r="3"/><path d="M22 9v10M22 25v10M9 22h10M25 22h10"/></svg>
    Hardware<br>Installation
  </div>
  <div class="tile" style="left:289px">
    <svg width="50" height="44" viewBox="0 0 50 44" fill="none" stroke="#1d4f8f" stroke-width="2"><rect x="4" y="14" width="18" height="24" rx="2"/><rect x="28" y="14" width="18" height="24" rx="2"/><circle cx="13" cy="26" r="5"/><circle cx="37" cy="26" r="5"/><path d="M13 4v6M25 2v8M37 4v6"/></svg>
    Currency<br>Mining
  </div>
  <div class="tile" style="left:448px">
    <svg width="46" height="44" viewBox="0 0 46 44" fill="none" stroke="#1d4f8f" stroke-width="2"><circle cx="23" cy="22" r="12"/><circle cx="23" cy="22" r="7"/><path d="M23 2v8M23 34v8M3 22h8M35 22h8M8 8l6 6M38 8l-6 6M8 36l6-6M38 36l-6-6"/></svg>
    Crypto<br>Earnings
  </div>
  <div class="tile" style="left:607px">
    <svg width="50" height="44" viewBox="0 0 50 44" fill="none" stroke="#1d4f8f" stroke-width="2"><path d="M12 34H9a7 7 0 0 1 0-14 12 12 0 0 1 23-4 9 9 0 0 1 9 18h-3"/><circle cx="30" cy="30" r="8"/><path d="M18 28v10M22 24v14"/></svg>
    Earn Crypto<br>Every Month
  </div>
  <div class="tile" style="left:766px">
    <svg width="44" height="44" viewBox="0 0 44 44" fill="none" stroke="#1d4f8f" stroke-width="2"><circle cx="22" cy="22" r="7"/><path d="M19 3h6l1 5 4 2 4-3 4 4-3 4 2 4 5 1v6l-5 1-2 4 3 4-4 4-4-3-4 2-1 5h-6l-1-5-4-2-4 3-4-4 3-4-2-4-5-1v-6l5-1 2-4-3-4 4-4 4 3 4-2z"/></svg>
    Service &amp;<br>Maintenance
  </div>
  <div class="tile" style="left:926px">
    <svg width="44" height="44" viewBox="0 0 44 44" fill="none" stroke="#1d4f8f" stroke-width="2"><path d="M22 3v38M5 12l34 20M39 12L5 32"/><circle cx="22" cy="22" r="4"/><circle cx="22" cy="4" r="2"/><circle cx="22" cy="40" r="2"/></svg>
    Flexible<br>Mining
  </div>

  <div class="service-art" role="img" aria-label="Isometric illustration of a mining server platform with small workers"></div>
  <div class="service-copy">
    <h3>Hardware Installation</h3>
    <p>In the last few years, the technology required to ‘mine’ crypto has fallen significantly and the speed and ability has increased. Our team acquire the latest technology and build a custom mining rig for you based on your investment criteria. The rig runs itself, you don’t need to do anything.</p>
  </div>
</section>

<section class="welcome">
  <div class="welcome-art" role="img" aria-label="Rows of mining rigs with glowing red cooling fans"></div>
  <span class="kicker">WELCOME TO</span>
  <h2>LEDGER HALCYON</h2>
  <span class="rule light" style="left:129px;top:150px"></span>
  <p>Martin and Nikola were part of the core team that built Duncan has been running IT and Operation teams of large companies for many years before setting up his own IT and Security Consultancy. Together this team know how to build, run and scale technology in Crypto and Payments, we only make 10% of your profits so we’re dedicated to make your Third Heron mining rigs perform.</p>
  <span class="btn btn-white" style="left:131px;top:420px;width:118px;height:39px">READ MORE</span>
</section>

<section class="team">
  <h2 class="section-title" style="top:50px">OUR TEAM</h2>
  <span class="rule" style="left:570px;top:99px"></span>

  <article class="member" style="left:131px">
    <div class="photo" role="img" aria-label="Portrait photo of co-founder Martin Keller"></div>
    <h4>MARTIN KELLER</h4>
    <p>Co-Founder who operates the business licenses, accounts and financial service partnerships.</p>
    <span class="btn btn-blue">VIEW BIO&nbsp;&nbsp;›</span>
  </article>
  <article class="member" style="left:452px">
    <div class="photo" style="background:linear-gradient(160deg,#f2f2f2,#c9cbcc 60%,#7d8084)" role="img" aria-label="Portrait photo of co-founder Duncan Fraser"></div>
    <h4>DUNCAN FRASER</h4>
    <p>Co-Founder who designs, builds and maintains our hardware and software solutions.</p>
    <span class="btn btn-blue">VIEW BIO&nbsp;&nbsp;›</span>
  </article>
  <article class="member" style="left:773px">
    <div class="photo" style="background:linear-gradient(160deg,#e9eef3,#a8b5c2 55%,#2f3a48)" role="img" aria-label="Photo of the trading team at work"></div>
    <h4>PETAR &amp; NIKOLA RADEV</h4>
    <p>Our Technology and Operations gurus who track the crypto markets daily.</p>
    <span class="btn btn-blue">VIEW BIO&nbsp;&nbsp;›</span>
  </article>
</section>

<section class="sells">
  <div class="gpu-art" role="img" aria-label="Graphics card with twin cooling fans"></div>
  <h3>SELLS CRYPTO MINING</h3>
  <span class="rule" style="left:619px;top:100px"></span>
  <p>Sed ut perspiciatis unde omnis iste natus error sit volupt atem accusantium doloremque laudantium, totam rem aperiam, eaque ipsa quae ab illo inventore veritatis et quasi architecto beatae vitae dicta sunt explicabo. Nemo enim ipsam voluptatem quia voluptas sit aspernatur aut odit aut fugit, sed quia consequuntur magni dolores eos qui ratione voluptatem sequi nesciunt.</p>
  <span class="btn btn-blue" style="left:619px;top:367px;width:118px;height:42px">READ MORE</span>
</section>

<section class="testimonials">
  <h2 class="section-title" style="top:48px">TESTIMONIALS</h2>
  <span class="rule light" style="left:570px;top:97px"></span>

  <blockquote class="quote" style="left:129px">
    <div class="mark">“</div>
    <p>“I’d been hearing a few mates on the golf course tell me how they had bought crypto currency a few years ago and now were enjoying the returns, I though I’d missed the boat. Martin explained that now crypto is mainstream, and technology has advanced massively, I didn’t need to be a millionaire with a warehouse in Iceland to participate. Since investing in my own mining rig, it sits in my spare room and returns about 4,700 AED each month.”</p>
    <cite>CANADIAN PILOT, SKYREACH AIRWAYS</cite>
  </blockquote>
  <blockquote class="quote" style="left:457px">
    <div class="mark">“</div>
    <p>“I’ve known Duncan for years so when he said he’d teamed up with Martin, the seasoned and succesful finTech entrepreneur, I knew I had to get in on the action. Since buying a Quartz rig, I am a convert of watching it make me Nimbuscoin and I’m enjoying it grow in value every month as it hits my account. Early retirement plans just became real!”</p>
    <cite>CANADIAN PILOT, SKYREACH AIRWAYS</cite>
  </blockquote>
  <blockquote class="quote" style="left:773px">
    <div class="mark">“</div>
    <p>I had 10 thousands pounds saved but going nowhere. Duncan explained that could buy a mining rig so I decided to invest it in the hardware. He came around himself, took about 2 hours to set it up, showed me how to open a CoinHarbor account and how to check the daily performance on my mobile or laptop. I can’t quite believe it’s making me money for what looks like nothing.</p>
    <cite>OFFICE MANAGER | DUBAI BUSINESS</cite>
  </blockquote>
</section>
<svg class="arrow" style="left:70px" width="18" height="26" viewBox="0 0 18 26" aria-label="Previous"><path d="M14 2 L4 13 L14 24" fill="none" stroke="#fff" stroke-width="3"/></svg>
<svg class="arrow" style="left:1108px" width="18" height="26" viewBox="0 0 18 26" aria-label="Next"><path d="M4 2 L14 13 L4 24" fill="none" stroke="#fff" stroke-width="3"/></svg>

<section class="faq">
  <h2 class="section-title" style="top:58px">FAQ</h2>
  <span class="rule" style="left:570px;top:104px"></span>

  <div class="q" style="left:129px;top:158px;height:49px">What do I need to support a Home Mining rig?<svg width="20" height="20" viewBox="0 0 20 20"><circle cx="10" cy="10" r="10" fill="var(--blue-deep)"/><path d="M6 8l4 4 4-4" fill="none" stroke="#fff" stroke-width="2"/></svg></div>
  <div class="q" style="left:607px;top:158px;height:49px">Isn’t Crypto Mining really bad for the planet?<svg width="20" height="20" viewBox="0 0 20 20"><circle cx="10" cy="10" r="10" fill="var(--blue-deep)"/><path d="M6 8l4 4 4-4" fill="none" stroke="#fff" stroke-width="2"/></svg></div>
  <div class="q" style="left:129px;top:225px;height:50px">What is The Flippening?<svg width="20" height="20" viewBox="0 0 20 20"><circle cx="10" cy="10" r="10" fill="var(--blue-deep)"/><path d="M6 8l4 4 4-4" fill="none" stroke="#fff" stroke-width="2"/></svg></div>
  <div class="q" style="left:607px;top:225px;height:50px">Will Third Heron Mining still work with Proof of Stake?<svg width="20" height="20" viewBox="0 0 20 20"><circle cx="10" cy="10" r="10" fill="var(--blue-deep)"/><path d="M6 8l4 4 4-4" fill="none" stroke="#fff" stroke-width="2"/></svg></div>
  <div class="q" style="left:129px;top:291px;height:70px">What is the difference between Proof of Work and Proof of Stake?<svg width="20" height="20" viewBox="0 0 20 20"><circle cx="10" cy="10" r="10" fill="var(--blue-deep)"/><path d="M6 8l4 4 4-4" fill="none" stroke="#fff" stroke-width="2"/></svg></div>
  <div class="q" style="left:607px;top:291px;height:70px"><span>EIP 1559? The reduction of gas fees to stay competitive<br>and reduce supply.</span><svg width="20" height="20" viewBox="0 0 20 20"><circle cx="10" cy="10" r="10" fill="var(--blue-deep)"/><path d="M6 8l4 4 4-4" fill="none" stroke="#fff" stroke-width="2"/></svg></div>
</section>

<section class="cta">
  <p>Sed ut perspiciatis unde omnis iste natus error sit voluptatem accusan tium doloremque laudantium</p>
  <span class="btn btn-blue">GET IN TOUCH</span>
</section>

<footer class="site-footer">
  <div class="logo abs" style="left:129px;top:44px;font-size:34px"><span class="logo-mark" style="width:44px;height:44px"></span>LEDGER HALCYON</div>
  <span class="follow">FOLLOW US ON</span>
  <span class="social" style="left:955px" aria-label="Social profile"></span>
  <span class="social" style="left:996px" aria-label="Social profile"></span>
  <span class="social" style="left:1039px;background:#1b2a63" aria-label="Social profile"></span>
  <nav class="nav">
    <a style="left:667px;top:114px">HOME</a>
    <a style="left:771px;top:114px">SERVICES</a>
    <a style="left:911px;top:114px">FAQ</a>
    <a style="left:997px;top:114px">CONTACT</a>
  </nav>
  <div class="line"></div>
  <p class="copy">Copyright © 2021 All Rights Reserved</p>
</footer>

</body>
</html>
```